Brisbane IT support business needs our first letterhead (Contest)

Hello we are a Brisbane based Information Technology company providing support and services to small and medium sized businesses. We provide a range of services and solutions.

The business name is Harlowe Network Computing Services, or HNCS for short.

I am looking for a letterhead that looks professional (don't we all want that), but most importantly, it most utilize the colours in the logo attached, and any text used preferably in font type: HandelGotDBol.

```html
<!DOCTYPE html>
<html lang="en">
<head>
<meta charset="utf-8">
<title>HNCS Stationery</title>
<link rel="stylesheet" href="https://fonts.googleapis.com/css2?family=Michroma&family=EB+Garamond&display=swap">
<style>
  :root {
    --backdrop: #f1dcc1;
    --teal: #01445d;
    --orange: #ec7d26;
    --paper: #ffffff;
    --rule: #c9c9c9;
    --watermark: #f1f4f6;
    --ink: #111111;
  }
  * { margin: 0; padding: 0; box-sizing: border-box; }
  html, body { width: 1200px; height: 900px; overflow: hidden; }
  body { background: var(--backdrop); position: relative; font-family: "Michroma", sans-serif; }

  .letterhead {
    position: absolute; left: 460px; top: 79px; width: 548px; height: 776px;
    background: var(--paper);
    box-shadow: 3px 4px 6px rgba(0,0,0,0.35);
    overflow: hidden;
  }
  .letterhead-brand {
    position: absolute; left: 150px; top: 52px;
    color: var(--orange); line-height: 1;
  }
  .letterhead-brand .brand-short { font-size: 44px; letter-spacing: 1px; }
  .letterhead-brand .brand-full { font-size: 9px; margin-top: 4px; width: 140px; line-height: 1.25; }
  .header-rule { position: absolute; left: 0; right: 0; top: 136px; height: 1px; background: var(--rule); }
  .watermark {
    position: absolute; left: 130px; top: 252px; width: 304px; height: 304px;
    border-radius: 50%; background: var(--watermark);
  }
  .contact-band {
    position: absolute; left: 0; right: 0; top: 636px; height: 115px;
    background: var(--orange);
    font-family: "EB Garamond", serif; color: var(--ink); font-size: 19px; line-height: 21px;
  }
  .contact-address { position: absolute; left: 16px; top: 64px; }
  .contact-lines { position: absolute; right: 10px; top: 46px; text-align: right; }

  .cover {
    position: absolute; left: 139px; top: 52px; width: 516px; height: 728px;
    background: var(--teal);
    box-shadow: 3px 4px 6px rgba(0,0,0,0.4);
  }
  .cover-mark {
    position: absolute; left: 88px; top: 308px; width: 126px; height: 126px;
    border-radius: 50%; background: var(--paper);
  }
  .cover-divider { position: absolute; left: 233px; top: 328px; width: 2px; height: 86px; background: var(--paper); }
  .cover-brand { position: absolute; left: 256px; top: 334px; color: var(--paper); line-height: 1; }
  .cover-brand .brand-short { font-size: 56px; letter-spacing: 2px; }
  .cover-brand .brand-full { font-size: 10px; margin-top: 6px; width: 190px; line-height: 1.3; }
</style>
</head>
<body>
  <section class="letterhead">
    <div class="letterhead-brand">
      <div class="brand-short">HNCS</div>
      <div class="brand-full">HARLOWE NETWORK COMPUTING SERVICES</div>
    </div>
    <div class="header-rule"></div>
    <div class="watermark"></div>
    <footer class="contact-band">
      <div class="contact-address">Sample Street</div>
      <div class="contact-lines">
        Tel: 123-555-984<br>
        Fax: 123-456-78<br>
        Email: office@hncs-mail.net
      </div>
    </footer>
  </section>

  <section class="cover">
    <div class="cover-mark"></div>
    <div class="cover-divider"></div>
    <div class="cover-brand">
      <div class="brand-short">HNCS</div>
      <div class="brand-full">HARLOWE NETWORK COMPUTING SERVICES</div>
    </div>
  </section>
</body>
</html>
```